Author needs website header

I want a website header that shows me as an author with a attractive tagline and highlights my new book with a Call to Action to get a Free Chapter

Call

```html
<!DOCTYPE html>
<html lang="en">
<head>
<meta charset="utf-8">
<title>Lorena Abiodun – Home</title>
<link href="https://fonts.googleapis.com/css2?family=Roboto:ital,wght@0,400;0,500;0,700;1,700&family=Tinos&family=Cormorant+Garamond:wght@500&family=Dancing+Script&family=Varela+Round&display=swap" rel="stylesheet">
<style>
  :root{
    --ink:#111;
    --line:#c9ced4;
    --panel-border:#d6d6d6;
    --fb:#0d5aa8;
    --tw:#4fc3ef;
    --mail:#8e8e8e;
    --print:#cfcfcf;
    --hero-dark:#0c1622;
    --teal:#27c3cf;
    --orange:#f57d0b;
    --link:#1a5fb4;
    --muted:#444;
    --icon-bg:#ececec;
    --icon-fg:#b8b8b8;
  }
  *{box-sizing:border-box;margin:0;padding:0}
  html,body{width:1200px;height:1200px;overflow:hidden;background:#fff}
  body{position:relative;font-family:"Roboto",Arial,sans-serif;color:var(--ink)}
  .abs{position:absolute}

  .top-rule{left:0;top:76px;width:1200px;height:1px;background:var(--line)}
  .social-top{left:1040px;top:86px;display:flex;gap:10px;font-size:12px;font-weight:500;color:#555}
  .social-top span{display:flex;align-items:center;gap:4px}
  .social-top i{width:10px;height:10px;background:#555;display:inline-block}

  .main-panel{left:30px;top:136px;width:738px;height:1000px;border:1px solid var(--panel-border);border-bottom:none;border-radius:3px 3px 0 0}
  .page-title{left:58px;top:168px;font-size:29px;font-weight:500}

  .share-bar{left:58px;top:215px;width:682px;height:34px;display:flex}
  .share-bar div{flex:1;display:flex;align-items:center;justify-content:center;gap:8px;color:#fff;font-size:13px}
  .share-fb{background:var(--fb)} .share-tw{background:var(--tw)}
  .share-mail{background:var(--mail)} .share-print{background:var(--print)}
  .share-bar i{width:14px;height:14px;background:#fff;border-radius:2px;display:inline-block;opacity:.9}

  .brand-name{left:60px;top:316px;font-family:"Tinos",serif;font-size:26px;color:#333}
  .brand-sub{left:88px;top:349px;font-family:"Tinos",serif;font-size:7px;letter-spacing:1.5px;color:#555}
  .tagline{left:520px;top:308px;width:220px;text-align:right;font-family:"Dancing Script",cursive;font-size:18px;line-height:23px;color:#222}

  .hero{left:58px;top:420px;width:690px;height:444px;background:radial-gradient(circle at 60% 20%,#165a66 0%,#0f2631 40%,var(--hero-dark) 75%);overflow:hidden}
  .hero-title{left:42px;top:38px;font-family:"Tinos",serif;color:#fff;font-size:32px;letter-spacing:.5px;white-space:nowrap}
  .hero-title small{font-size:26px}
  .hero-title b{font-weight:400;color:var(--teal);font-size:52px}
  .book-art{left:30px;top:92px;width:212px;height:268px;background:linear-gradient(135deg,#e9eef3,#b9cbe0 60%,#7fa66a);border-radius:2px}
  .order-badge{left:228px;top:292px;width:56px;height:56px;border-radius:50%;background:var(--teal);border:2px dashed #fff;color:#fff;font-family:"Dancing Script",cursive;font-size:17px;line-height:18px;text-align:center;padding-top:9px}
  .hero-copy{left:250px;top:146px;width:200px;text-align:center;font-family:"Tinos",serif;color:#fff;font-size:23px;line-height:23px}
  .hero-copy p+p{margin-top:24px}
  .author-photo{left:438px;top:0;width:252px;height:444px;background:linear-gradient(180deg,#1a4048 0%,#6a6f78 45%,#9aa3ad 70%,#1a1a1f 100%)}
  .field{height:20px;background:#fff;border-left:6px solid var(--teal);border-right:14px solid var(--teal);font-family:"Tinos",serif;font-size:13px;color:#aaa;padding:2px 4px;top:376px}
  .field-name{left:38px;width:198px}
  .field-email{left:262px;width:196px;padding-left:14px}
  .submit{left:468px;top:366px;width:168px;height:40px;border-radius:20px;background:var(--orange);color:#111;font-family:"Tinos",serif;font-size:25px;display:flex;align-items:center;justify-content:center}
  .hero-link{left:273px;top:410px;font-family:"Tinos",serif;font-size:14px;color:var(--orange)}

  .feature{width:180px;text-align:center;top:900px}
  .feature-icon{width:72px;height:72px;border-radius:50%;background:var(--icon-bg);margin:0 auto;display:flex;align-items:center;justify-content:center}
  .feature h3{margin-top:36px;font-size:13px;font-style:italic;font-weight:700}
  .feature p{margin-top:6px;font-family:"Varela Round",sans-serif;font-size:14px;line-height:22.5px;color:var(--muted)}
  .main-foot{left:58px;top:1121px;width:682px;height:2px;background:#e4e4e4}

  .search{left:794px;top:136px;width:350px;height:32px;border:2px solid #d5d5d5;border-radius:16px;display:flex;align-items:center;gap:6px;padding-left:8px;font-size:12px;color:#c4c4c4}
  .widget{left:794px;width:350px;border:2px solid #ddd;border-radius:3px;background:#fff}
  .widget h2{background:#000;color:#fff;font-size:17px;font-weight:700;text-align:center;height:56px;line-height:56px}
  .widget li{list-style:none;height:41px;line-height:41px;padding-left:12px;font-family:"Cormorant Garamond",serif;font-weight:500;font-size:13px;color:var(--link);border-top:1px solid #e2e2e2}
  .widget li:first-child{border-top:none}
</style>
</head>
<body>
  <div class="abs top-rule"></div>
  <div class="abs social-top"><span><i></i>Chirper</span><span><i></i>Friendbook</span></div>

  <div class="abs main-panel"></div>
  <h1 class="abs page-title">Home</h1>

  <div class="abs share-bar">
    <div class="share-fb"><i></i>537</div>
    <div class="share-tw"><i></i>Chirp</div>
    <div class="share-mail">
      <svg width="30" height="20" viewBox="0 0 30 20"><rect x="1" y="1" width="28" height="18" fill="none" stroke="#fff" stroke-width="2"/><path d="M1 1 L15 12 L29 1 M1 19 L12 9 M29 19 L18 9" fill="none" stroke="#fff" stroke-width="2"/></svg>Email</div>
    <div class="share-print">
      <svg width="24" height="20" viewBox="0 0 24 20"><rect x="6" y="1" width="12" height="5" fill="#fff"/><rect x="1" y="6" width="22" height="9" rx="2" fill="#fff"/><rect x="6" y="13" width="12" height="6" fill="#fff" stroke="#cfcfcf"/></svg>Print</div>
  </div>

  <div class="abs brand-name">Lorena Abiodun</div>
  <div class="abs brand-sub">TEACHER AUTHOR, PREACHER</div>
  <div class="abs tagline">Hi I'm Lorena Abiodun, join me in keeping on and beginning again!</div>

  <section class="abs hero">
    <div class="abs book-art" role="img" aria-label="Three-dimensional stack of the book Hearing the Quiet Call"></div>
    <div class="abs order-badge">Order<br>Now</div>
    <div class="abs author-photo" role="img" aria-label="Portrait photo of the author smiling"></div>
    <div class="abs hero-title">HEARING <small>THE</small> QUIET <b>CALL</b></div>
    <div class="abs hero-copy"><p>A journey in discovering divine</p><p>opportunities in unexpected places</p></div>
    <div class="abs field field-name">Name</div>
    <div class="abs field field-email">✉&nbsp; Email Address</div>
    <div class="abs submit">SUBMIT</div>
    <div class="abs hero-link">Get My eBook For Free</div>
  </section>

  <div class="abs feature" style="left:38px">
    <div class="feature-icon"><svg width="40" height="30" viewBox="0 0 40 30"><path d="M2 10 L12 4 L20 8 L28 4 L38 10 L30 22 L20 26 L10 22 Z" fill="var(--icon-fg)"/></svg></div>
    <h3>Meet Lorena Abiodun</h3>
    <p>tempor incididunt ut labore et dolore magna aliqua.</p>
  </div>
  <div class="abs feature" style="left:218px">
    <div class="feature-icon"><svg width="34" height="34" viewBox="0 0 34 34"><circle cx="17" cy="17" r="15" fill="var(--icon-fg)"/><rect x="10" y="9" width="14" height="16" rx="2" fill="var(--icon-bg)"/><path d="M13 14h8M13 18h8M13 22h8" stroke="var(--icon-fg)" stroke-width="2"/></svg></div>
    <h3>My Blog</h3>
    <p>tempor incididunt ut labore et dolore magna aliqua.</p>
  </div>
  <div class="abs feature" style="left:398px">
    <div class="feature-icon"><svg width="30" height="40" viewBox="0 0 30 40"><circle cx="15" cy="5" r="4" fill="var(--icon-fg)"/><path d="M8 10h14l-2 6H10z" fill="var(--icon-fg)"/><path d="M3 16h24l-2 4h-5l-2 18h-6l-2-18H5z" fill="var(--icon-fg)"/></svg></div>
    <h3>Speaking</h3>
    <p>tempor incididunt ut labore et dolore magna aliqua.</p>
  </div>
  <div class="abs feature" style="left:578px">
    <div class="feature-icon"><svg width="40" height="32" viewBox="0 0 40 32"><path d="M2 4h22v14H12l-6 5v-5H2z" fill="var(--icon-fg)"/><path d="M16 10h22v14h-4v5l-6-5H16z" fill="var(--icon-fg)" stroke="var(--icon-bg)" stroke-width="2"/></svg></div>
    <h3>Contact Me</h3>
    <p>tempor incididunt ut labore et dolore magna aliqua.</p>
  </div>
  <div class="abs main-foot"></div>

  <div class="abs search">
    <svg width="16" height="16" viewBox="0 0 16 16"><circle cx="6.5" cy="6.5" r="5" fill="none" stroke="#999" stroke-width="2"/><path d="M10 10l5 5" stroke="#999" stroke-width="2"/></svg>Search my blog...
  </div>

  <aside class="abs widget" style="top:186px">
    <h2>Recent Posts</h2>
    <ul><li>Live Your Life To Please God</li><li>Jesus Loves You Very Much</li></ul>
  </aside>
  <aside class="abs widget" style="top:349px">
    <h2>Recent Comments</h2>
  </aside>
  <aside class="abs widget" style="top:431px">
    <h2>Archives</h2>
    <ul><li>September 2016</li></ul>
  </aside>
  <aside class="abs widget" style="top:552px">
    <h2>Categories</h2>
    <ul><li>Devotion</li></ul>
  </aside>
  <aside class="abs widget" style="top:674px">
    <h2>Meta</h2>
    <ul><li>Log in</li><li>Entries RSS</li><li>Comments RSS</li><li>SitePress.org</li></ul>
  </aside>
</body>
</html>
```